Piano teaching business needs a business card and logo design.

We provide piano lessons to children and adults. The card / logo should be colourful and playful and appeal to kids but retain a professional mature approach which also appeals to adults. I like the Colours orange and blue as dominating theme colours, but we are open to all colour ideas. The business name is: SLOW OWL BLUES. We do not like typical black and white images of piano keyboards. A cartoon character of a jazz inspired orange coloured fat cat playing piano is one idea but we are open to all ideas.

Target Market(s)

Domestic, Local population, adults and children.

Industry/Entity Type

Service

Contact Information for Business Card

Piano teacher
Mick L Vance
37 Wendle Crescent
Marlow Heights
4297 QLD
T: 07 5839 2417
M: 0438 702 965
E: keysbrel@examplemail.net
www. keysbrel.com.au

Logo Text

Slow Owl Blues

Font styles to use
Sans Serif

Colors
f78f20
f37122
0493ce
0455a3
fbed22

Requirements
Must have
• Colours.
Nice to have
• Cartoon style fat cat. Limited music notation.
Should not have
• Dominating images of keyboards.

```html
<!DOCTYPE html>
<html lang="en">
<head>
<meta charset="utf-8">
<title>Slow Owl Blues – Business Card</title>
<link rel="stylesheet" href="https://fonts.googleapis.com/css2?family=Arimo:wght@400;700&family=Oswald:wght@600&display=swap">
<style>
  :root {
    --stage: #0e0e0e;
    --card: #1b1b1c;
    --orange: #f78f20;
    --orange-deep: #f37122;
    --blue: #0493ce;
    --white: #f4f4f4;
    --rule: #4a4a4a;
  }
  * { box-sizing: border-box; margin: 0; padding: 0; }
  html, body {
    width: 1200px; height: 900px; overflow: hidden;
    background: var(--stage);
    font-family: "Arimo", Arial, sans-serif;
  }
  .stage {
    position: relative; width: 1200px; height: 900px;
    display: flex; flex-direction: column; align-items: center; justify-content: center; gap: 40px;
  }
  .card {
    position: relative; width: 620px; height: 340px;
    background: var(--card);
    box-shadow: 0 10px 30px rgba(0,0,0,.6);
    overflow: hidden;
  }
  .card__band {
    position: absolute; left: 0; right: 0; bottom: 0; height: 12px;
    background: var(--blue);
  }

  /* Front */
  .brand {
    position: absolute; left: 0; right: 0; top: 100px;
    display: flex; align-items: center; justify-content: center; gap: 22px;
  }
  .brand__dot {
    width: 74px; height: 74px; border-radius: 50%;
    background: var(--blue);
  }
  .brand__name {
    font-weight: 700; font-size: 44px; color: var(--orange);
    letter-spacing: .5px; white-space: nowrap;
  }
  .tagline {
    position: absolute; left: 0; right: 0; bottom: 38px;
    display: flex; justify-content: center; gap: 12px;
    list-style: none; color: var(--white); font-size: 16px; letter-spacing: .3px;
    white-space: nowrap;
  }
  .tagline li::before {
    content: ""; display: inline-block; width: 7px; height: 7px; border-radius: 50%;
    background: var(--orange); margin-right: 7px; vertical-align: middle; position: relative; top: -2px;
  }

  /* Back */
  .person {
    position: absolute; left: 56px; top: 124px; width: 236px; text-align: center;
  }
  .person__name {
    font-family: "Oswald", "Arial Narrow", sans-serif; font-weight: 600;
    font-size: 38px; line-height: 1; color: var(--orange-deep); text-transform: uppercase;
    white-space: nowrap;
  }
  .person__role { margin-top: 4px; font-size: 17px; color: var(--white); letter-spacing: .4px; }
  .divider {
    position: absolute; left: 308px; top: 100px; width: 1px; height: 110px; background: var(--rule);
  }
  .contacts {
    position: absolute; left: 328px; top: 104px; list-style: none;
    color: var(--white); font-size: 17px; line-height: 26px; letter-spacing: .4px;
    white-space: nowrap;
  }
  .contacts li { display: flex; align-items: center; gap: 9px; }
  .contacts svg { width: 15px; height: 15px; flex: none; }
  .address {
    position: absolute; left: 78px; bottom: 38px;
    color: var(--white); font-size: 17px; letter-spacing: .4px; white-space: nowrap;
  }
</style>
</head>
<body>
<main class="stage">

  <section class="card card--front">
    <div class="brand">
      <span class="brand__dot"></span>
      <span class="brand__name">Slow Owl Blues</span>
    </div>
    <ul class="tagline">
      <li>Play for fun</li>
      <li>Simplify songs</li>
      <li>Chords...</li>
      <li>Improvisation</li>
    </ul>
    <div class="card__band"></div>
  </section>

  <section class="card card--back">
    <div class="person">
      <h1 class="person__name">Mick L Vance</h1>
      <p class="person__role">Piano teacher</p>
    </div>
    <div class="divider"></div>
    <ul class="contacts">
      <li>
        <svg viewBox="0 0 16 16" aria-hidden="true"><path d="M3.5 1.5l2.5 0 1 3.5-1.6 1.2a8 8 0 0 0 4.4 4.4L11 9l3.5 1v2.5c0 1-1 2-2 2A11 11 0 0 1 1.5 3.5c0-1 1-2 2-2z" fill="var(--orange)"/></svg>
        07 5839 2417
      </li>
      <li>
        <svg viewBox="0 0 16 16" aria-hidden="true"><rect x="4" y="1" width="8" height="14" rx="1.5" fill="none" stroke="var(--orange)" stroke-width="1.6"/><circle cx="8" cy="12.5" r="0.9" fill="var(--orange)"/></svg>
        0438 702 965
      </li>
      <li>
        <svg viewBox="0 0 16 16" aria-hidden="true"><rect x="1" y="3.5" width="14" height="9" fill="var(--orange)"/><path d="M1 3.5l7 5 7-5" fill="none" stroke="var(--card)" stroke-width="1.2"/></svg>
        keysbrel@examplemail.net
      </li>
      <li>
        <svg viewBox="0 0 16 16" aria-hidden="true"><g fill="none" stroke="var(--orange)" stroke-width="1.3"><circle cx="8" cy="8" r="6.5"/><ellipse cx="8" cy="8" rx="2.8" ry="6.5"/><path d="M1.5 8h13M2.6 4.5h10.8M2.6 11.5h10.8"/></g></svg>
        www. keysbrel.com.au
      </li>
    </ul>
    <p class="address">37 Wendle Crescent Marlow Heights, 4297 QLD</p>
    <div class="card__band"></div>
  </section>

</main>
</body>
</html>
```